Packaging design for aloe lotion bottle for a Laser Clinic

We need a packaging design for a body lotion bottle. Our business is a laser clinic and we are looking at slowly rolling out a range of skincare products. This lotion bottle is the first item with more to follow so the winning designer will have other designs to work on in the future.

The design needs to be classy, elegant, strong and sophisticated. The bottle will be clear with a shiny silver sleeved lid. The lotion itself, which will be visible through the bottle, will be a very light green colour. Think Mirelle Davonne and Voriel as that is the image I want to convey.

Ideally we were thinking of having a design with a single colour but if you come up with a fantastic multi colour design that we love then we're open to it.

Reason: I have extended the deadline as I feel I need more time to allow designers to submit their designs. I haven't found a design that I love just yet. The project has been made a guaranteed payment upon completion. Thank you.

Target Market(s)

upper class high income earners with a high disposable income. People that look after themselves

Industry/Entity Type

Beauty Salon

Colors
000000
cadf82

Requirements
Must have
• must include the details below:
• Post Laser Calming Cream
• This soothing and calming anti inflammatory cream is specifically formulated for use after post laser treatments.
• Fresh Cucumber, Melon and Aloe Vera Leaf Juice blend together in perfect harmony to quickly cool you skin and restore your skins natural moisture.
• Our luxurious calming cream targets redness and helps to reduce inflammation, bringing you supple and radiant skin like never before.
• Directions: Use a liberal amount twice daily on all your treatment areas. This nourishing cream can also be used daily to restore moisture and softness to areas of the face and body not being treated by laser or IPL.
• Ingredients: water (aqua), glycine soja (soybean) oil, cetyl alcohol, glycerin dimethicone, butyrospermum parkii (shea butter), theobroma cacao (cocoa) seed butter, aloe barbadensis (aloe vera) leaf juice, tocopheryl acetate, sodium ascorbyl phosphate, disodium EDTA, ceteareth-20, carbomer, BHT, benzyl benzoate, butylphenyl methylpropional, hexyl cinnamal, linalool, glyceryl caprylate, methylisothiazolinone. May contain: Red 4 (CI 14700, aka 504), Yellow 5 (CI 19140, Ki4), Yellow 6 (CI 15985, KI5), Blue 1 (CI 42090, Ao1), Red 33 (CI 17200, Aka 227), Ext. Violet 2 (CI 60730, Murasaki401), Green 3 (CI 42053, Midori3)
• Against Animal Testing
• Manufactured in Australia
• www.velvetglowclinic.com.au
• 500ml
• Pure Halo Laser Hair Removal logo (see attached files)
Nice to have
• A sophisticated and elegant design
Should not have
• no photos. not too many different colours

```html
<!DOCTYPE html>
<html lang="en">
<head>
<meta charset="utf-8">
<title>Post Laser Calming Cream – Label Design</title>
<link rel="stylesheet" href="https://fonts.googleapis.com/css2?family=Cormorant+Garamond:wght@500;600&family=Barlow:wght@400;500&display=swap">
<style>
  :root {
    --canvas: #ffffff;
    --label: #f2f2f2;
    --label-edge: #e2e2e2;
    --green: #5e9f4c;
    --ink: #111111;
    --body: #6d6d6d;
    --serif: "Cormorant Garamond", "Times New Roman", serif;
    --sans: "Barlow", "Helvetica Neue", Arial, sans-serif;
  }
  * { box-sizing: border-box; margin: 0; padding: 0; }
  html, body { width: 1045px; height: 1200px; overflow: hidden; background: var(--canvas); }
  .canvas { position: relative; width: 1045px; height: 1200px; }

  .label {
    position: absolute;
    width: 180px; height: 250px;
    background: linear-gradient(90deg, var(--label-edge) 0%, var(--label) 12%, #fafafa 50%, var(--label) 88%, var(--label-edge) 100%);
    font-family: var(--sans);
    color: var(--body);
    overflow: hidden;
  }

  /* vertical front labels */
  .vertical-copy {
    position: absolute;
    writing-mode: vertical-rl;
    transform: rotate(180deg);
    display: flex;
    gap: 6px;
  }
  .title {
    font-family: var(--serif);
    font-weight: 500;
    color: var(--green);
    text-transform: uppercase;
    line-height: .86;
    letter-spacing: .01em;
  }
  .blurb {
    font-size: 7px;
    line-height: 1.3;
    text-transform: uppercase;
    letter-spacing: .04em;
  }
  .volume {
    position: absolute;
    font-size: 7px;
    letter-spacing: .04em;
    color: var(--ink);
  }

  /* brand mark: name set in the body type with a plain square */
  .brand {
    position: absolute;
    display: flex;
    align-items: center;
    gap: 4px;
    font-family: var(--sans);
    font-weight: 500;
    font-size: 7px;
    letter-spacing: .08em;
    color: var(--ink);
    text-transform: uppercase;
    white-space: nowrap;
  }
  .brand::before {
    content: "";
    width: 7px; height: 7px;
    background: var(--ink);
  }

  /* flat wrap panels */
  .panel-copy {
    position: absolute;
    left: 28px; right: 18px;
    font-size: 6px;
    line-height: 1.75;
    text-transform: uppercase;
    letter-spacing: .04em;
  }
  .panel-copy p + p { margin-top: 9px; }
  .front-title { font-size: 27px; }
  .front-blurb { font-size: 7.4px; line-height: 1.45; margin-top: 8px; }

  .back-info {
    position: absolute;
    left: 80px; bottom: 36px;
    writing-mode: vertical-rl;
    transform: rotate(180deg);
    font-size: 6px;
    line-height: 1.8;
    text-transform: uppercase;
    letter-spacing: .04em;
  }
</style>
</head>
<body>
<main class="canvas">

  <!-- front concept A -->
  <section class="label" style="left:56px; top:180px;">
    <div class="vertical-copy" style="left:66px; top:20px; height:186px;">
      <h2 class="title" style="font-size:25px;">Post Laser<br>Calming Cream</h2>
      <p class="blurb">This soothing and calming<br>anti inflammatory cream<br>is specifically formulated<br>for use after post laser<br>treatments.</p>
    </div>
    <div class="brand" style="left:10px; top:200px;">Pure Halo</div>
    <span class="volume" style="left:80px; top:232px;">500ML</span>
  </section>

  <!-- front concept B -->
  <section class="label" style="left:315px; top:180px;">
    <div class="vertical-copy" style="left:56px; top:36px; height:150px;">
      <h2 class="title" style="font-size:25px;">Post Laser<br>Calming<br>Cream</h2>
      <p class="blurb">This soothing and calming<br>anti inflammatory cream<br>is specifically formulated<br>for use after post laser<br>treatments.</p>
    </div>
    <div class="brand" style="left:10px; top:214px;">Pure Halo</div>
    <span class="volume" style="left:80px; top:232px;">500ML</span>
  </section>

  <!-- front concept C -->
  <section class="label" style="left:562px; top:180px;">
    <div class="vertical-copy" style="left:24px; top:44px; height:150px;">
      <h2 class="title" style="font-size:27px;">Post Laser<br>Calming<br>Cream</h2>
      <p class="blurb">This soothing and calming<br>anti inflammatory cream<br>is specifically formulated<br>for use after post laser<br>treatments.</p>
    </div>
    <div class="brand" style="left:68px; top:224px;">Pure Halo</div>
    <span class="volume" style="left:142px; top:225px;">500ML</span>
  </section>

  <!-- wrap: front -->
  <section class="label" style="left:56px; top:712px;">
    <div class="panel-copy" style="top:40px; left:20px;">
      <h2 class="title front-title">Post Laser<br>Calming<br>Cream</h2>
      <p class="front-blurb">This soothing and calming<br>anti inflammatory cream<br>is specifically formulated<br>for use after post laser<br>treatments.</p>
    </div>
    <div class="brand" style="left:58px; top:216px;">Pure Halo</div>
    <span class="volume" style="left:146px; top:216px;">500ML</span>
  </section>

  <!-- wrap: story and directions -->
  <section class="label" style="left:284px; top:712px;">
    <div class="panel-copy" style="top:40px;">
      <p>Fresh cucumber, melon and aloe vera leaf juice blend together in perfect harmony to quickly cool you skin and restore your skins natural moisture.</p>
      <p>- Our luxurious calming cream targets redness and helps to reduce inflammation, bringing you supple and radiant skin like never before.</p>
      <p>- Directions: use a liberal amount twice daily on all your treatment areas. This nourishing cream can also be used daily to restore moisture and softness to areas of the face and body not being treated by laser or IPL.</p>
    </div>
    <div class="brand" style="left:66px; top:222px;">Pure Halo</div>
  </section>

  <!-- wrap: ingredients -->
  <section class="label" style="left:528px; top:712px;">
    <div class="panel-copy" style="top:40px; font-size:5.2px; line-height:1.85;">
      <p>Ingredients: water (aqua), glycine soja (soybean) oil, cetyl alcohol, glycerin dimethicone, butyrospermum parkii (shea butter), theobroma cacao (cocoa) seed butter, aloe barbadensis (aloe vera) leaf juice, tocopheryl acetate, sodium ascorbyl phosphate, disodium EDTA, ceteareth-20, carbomer, BHT, benzyl benzoate, butylphenyl methylpropional, hexyl cinnamal, linalool, glyceryl caprylate, methylisothiazolinone. May contain: Red 4 (CI 14700, aka 504), Yellow 5 (CI 19140, Ki4), Yellow 6 (CI 15985, Ki5), Blue 1 (CI 42090, Ao1), Red 33 (CI 17200, aka 227), Ext. Violet 2 (CI 60730, Murasaki401), Green 3 (CI 42053, Midori3)</p>
    </div>
  </section>

  <!-- wrap: back info -->
  <section class="label" style="left:764px; top:712px;">
    <p class="back-info">Against animal testing<br>Manufactured in Australia<br>www.velvetglowclinic.com.au</p>
  </section>

</main>
</body>
</html>
```